Welcome to the neighborhood

We need two post card designs for Marsh and Fern Insurance Company.

The first one is when someone moves into a new home.
We want it to include the following:

Congratulations and welcome to the neighborhood.
We are a local independent insurance agency established in 1912
Please let us know if we can be of service to you.

Second post card to send after 6 months in the area should include the following:

Just to let you know................

Marsh and Fern Insurance Agency was established over 100 years ago.
We are in the neighborhood and would appreciate the opportunity to provide you with a no obligation insurance review.
We will offer multiple quotes from several A rated insurance companies and will give you a $10.00 Brewlark gift card to quote your home and auto insurance.
We have saved hundreds of dollars for our clients by offering more coverage at a lower premium.
Please let our professional staff help you with your insurance needs.

Target Market(s)

Individuals that own a home and cars

Industry/Entity Type

Insurance

Font styles to use
Serif

Requirements
Must have
• Marsh and Fern Logo - we have it on jpg file - we tried to attach it but it doesn't seem like it worked
Our colors are black and gold - please incorporate these colors on the postcard
Website www.marshandfern-example.com
Like us on Porchlight
Agency address and phone number
417 Quillon Avenue Suite 318
Lake Bluff, IL 60987
(847)555-0142
Nice to have
• Some visual appeal relative to the topic - home and car - people - somethinng creative

```html
<!DOCTYPE html>
<html lang="en">
<head>
<meta charset="utf-8">
<title>Marsh and Fern – Welcome Postcards</title>
<link rel="stylesheet" href="https://fonts.googleapis.com/css2?family=Libre+Bodoni:wght@400;500&family=Marcellus&display=swap">
<style>
  :root {
    --blue: #1f4f8a;
    --blue-deep: #0f305e;
    --blue-light: #4d78aa;
    --gold: #b89f5c;
    --gold-deep: #8c6d2c;
    --ink: #1c1c1c;
    --paper: #ffffff;
    --line: #d9d9d9;
    --headline: "Libre Bodoni", "Bodoni Moda", serif;
    --body: "Marcellus", "Optima", serif;
  }
  * { margin: 0; padding: 0; box-sizing: border-box; }
  html, body { width: 1200px; height: 970px; overflow: hidden; background: var(--paper); }
  .canvas { position: relative; width: 1200px; height: 970px; }

  .postcard {
    position: absolute;
    background: var(--paper);
    border: 1px solid var(--line);
    box-shadow: 0 2px 8px rgba(0,0,0,.12);
    overflow: hidden;
  }
  .mosaic-field {
    position: absolute; left: 0; top: 0; width: 100%;
    background:
      radial-gradient(ellipse at 75% 20%, rgba(120,155,200,.45), transparent 60%),
      linear-gradient(160deg, var(--blue-light) 0%, var(--blue) 45%, var(--blue-deep) 100%);
  }
  .gold-band {
    position: absolute; left: 0; width: 100%;
    background: linear-gradient(90deg, var(--gold) 0%, #c9b274 45%, var(--gold-deep) 100%);
    color: var(--paper);
    font-family: var(--body);
    text-align: center;
  }
  .brand {
    position: absolute; left: 50%; transform: translateX(-50%);
    display: flex; align-items: center; gap: 8px;
    font-family: var(--headline); font-weight: 500;
    color: var(--gold); letter-spacing: 1px; white-space: nowrap;
  }
  .brand-square { width: 10px; height: 10px; background: var(--gold); }
  .headline {
    position: absolute; left: 0; width: 100%;
    font-family: var(--headline); font-weight: 400; color: var(--paper);
    text-align: center; line-height: 1;
  }
  .message {
    position: absolute; left: 0; width: 100%;
    font-family: var(--body); color: var(--ink); text-align: center;
  }

  /* Card 1 – welcome */
  .card-welcome { left: 40px; top: 40px; width: 570px; height: 480px; }
  .card-welcome .mosaic-field { height: 292px; }
  .card-welcome .brand { top: 26px; font-size: 20px; }
  .card-welcome .headline { top: 100px; }
  .card-welcome .line-big { font-size: 62px; display: block; }
  .card-welcome .line-small { font-size: 30px; display: block; margin-top: 8px; }
  .card-welcome .line-mid { font-size: 46px; display: block; margin-top: 4px; }
  .card-welcome .gold-band { top: 292px; height: 44px; line-height: 44px; font-size: 19px; letter-spacing: 4px; }
  .card-welcome .message { top: 370px; font-size: 19px; line-height: 1.45; padding: 0 30px; }

  /* Card 2 – address side */
  .card-mailer { left: 615px; top: 120px; width: 570px; height: 510px; }
  .card-mailer .mosaic-field { width: 288px; height: 250px; }
  .card-mailer .brand { left: 144px; top: 28px; font-size: 15px; }
  .card-mailer .headline { width: 288px; top: 88px; font-size: 36px; line-height: 1.1; }
  .card-mailer .gold-band { top: 172px; width: 288px; height: 78px; padding-top: 16px; font-size: 14px; line-height: 1.3; }
  .return-address {
    position: absolute; left: 305px; top: 75px;
    font-family: var(--body); font-style: normal; font-size: 13px; line-height: 1.5; color: var(--ink);
  }
  .stamp-box { position: absolute; right: 28px; top: 84px; width: 84px; height: 74px; border: 2px solid var(--ink); }

  /* Card 3 – six months follow-up */
  .card-followup { left: 420px; top: 472px; width: 560px; height: 480px; }
  .card-followup .mosaic-field { height: 235px; }
  .card-followup .brand { top: 30px; font-size: 17px; }
  .card-followup .headline { top: 98px; font-size: 48px; line-height: 1.05; }
  .card-followup .gold-band { top: 235px; height: 36px; line-height: 36px; font-size: 17px; letter-spacing: 4px; }
  .card-followup .message { top: 288px; font-size: 13px; line-height: 1.45; padding: 0 56px; }
  .card-followup strong { font-weight: 700; font-family: var(--body); }
</style>
</head>
<body>
<main class="canvas">

  <section class="postcard card-welcome">
    <div class="mosaic-field" role="img" aria-label="Blue mosaic of soft squares as background"></div>
    <div class="brand"><span class="brand-square"></span>MARSH &amp; FERN</div>
    <h1 class="headline">
      <span class="line-big">Congratulations</span>
      <span class="line-small">and welcome to</span>
      <span class="line-mid">the neighborhood!</span>
    </h1>
    <div class="gold-band">www.marshandfern-example.com</div>
    <p class="message">We are a local independent insurance agency established<br>in 1912. Please let us know if we can be of service to you.</p>
  </section>

  <section class="postcard card-mailer">
    <div class="mosaic-field" role="img" aria-label="Blue mosaic of soft squares as background"></div>
    <div class="brand"><span class="brand-square"></span>MARSH &amp; FERN</div>
    <h2 class="headline">Like us on<br>Porchlight!</h2>
    <div class="gold-band">www.marshandfern-example.com<br>847-555-0142</div>
    <address class="return-address">417 Quillon Avenue<br>Suite 318<br>Lake Bluff, IL 60987</address>
    <div class="stamp-box"></div>
  </section>

  <section class="postcard card-followup">
    <div class="mosaic-field" role="img" aria-label="Blue mosaic of soft squares as background"></div>
    <div class="brand"><span class="brand-square"></span>MARSH &amp; FERN</div>
    <h2 class="headline">Just to<br>let you know...</h2>
    <div class="gold-band">www.marshandfern-example.com</div>
    <p class="message">Marsh and Fern Insurance Agency was established over 100 years ago. We are in the neighborhood and would appreciate the opportunity to provide you with a no obligation insurance review. We will offer multiple quotes from several A rated insurance companies and will give you a <strong>$10.00 Brewlark gift card</strong> to quote your home and auto insurance. We have saved hundreds of dollars for our clients by offering more coverage at a lower premium. Please let our professional staff help you with your insurance needs.</p>
  </section>

</main>
</body>
</html>
```